Velora aesthetics offers a range of facial aesthetics treatments by a fully qualified dentist, to a high end crowd. Treatments include antiwrinkle treatment, the use of dermal fillers to provide facial volumisation and rejuvenation and also lip volumisation.
I want a luxurious and bold look. Black background with a bold striking gold logo in the centre possibly incorporating the outline of a face in a subtle yet effective way. I want it to include the work I offer so people will be aware of what they are looking into but not look like there's too much on the card, So it's a clean look.
At the bottom I would like it to say by Dr. Anjali Desai. Alongside my email address and mobile number.

```html
<!DOCTYPE html>
<html lang="en">
<head>
<meta charset="utf-8">
<title>Velora Aesthetics – Business Card</title>
<link rel="stylesheet" href="https://fonts.googleapis.com/css2?family=Questrial&family=Pinyon+Script&family=Lato:wght@400;700&display=swap">
<style>
  :root {
    --page-bg: #2a2a2a;
    --card-bg: #151515;
    --brand-text: #e6e6e6;
    --gloss-dark: #3c3c3c;
    --gloss-light: #a8a8a8;
    --contact-text: #d2d2d2;
    --services-text: #6a6a6a;
    --rule-light: #d8d8d8;
    --rule-dark: #2a2a2a;
  }
  * { margin: 0; padding: 0; box-sizing: border-box; }
  html, body {
    width: 1200px;
    height: 997px;
    overflow: hidden;
    background: var(--page-bg);
  }
  .business-card {
    position: absolute;
    left: 150px;
    top: 241px;
    width: 900px;
    height: 515px;
    background: var(--card-bg);
    box-shadow: 0 20px 50px rgba(0,0,0,0.55);
    text-align: center;
  }
  .brand-name {
    position: absolute;
    top: 70px;
    width: 100%;
    font-family: "Questrial", sans-serif;
    font-weight: 400;
    font-size: 38px;
    letter-spacing: 1px;
    color: var(--brand-text);
  }
  .practitioner-name {
    position: absolute;
    top: 124px;
    left: 0;
    width: 100%;
    font-family: "Pinyon Script", cursive;
    font-size: 82px;
    line-height: 100px;
    background: linear-gradient(100deg, var(--gloss-dark) 0%, var(--gloss-dark) 35%, var(--gloss-light) 60%, #7a7a7a 80%, var(--gloss-light) 100%);
    -webkit-background-clip: text;
    background-clip: text;
    color: transparent;
  }
  .rule {
    position: absolute;
    height: 2px;
  }
  .rule--upper {
    left: 440px;
    right: 40px;
    top: 236px;
    background: linear-gradient(90deg, rgba(216,216,216,0), var(--rule-light));
  }
  .rule--lower {
    left: 40px;
    width: 450px;
    top: 462px;
    background: linear-gradient(90deg, var(--rule-dark), #5a5a5a);
  }
  .contact {
    position: absolute;
    top: 264px;
    width: 100%;
    font-family: "Lato", sans-serif;
    font-size: 22px;
    line-height: 38px;
    color: var(--contact-text);
  }
  .contact__label { font-weight: 700; }
  .services {
    position: absolute;
    top: 364px;
    width: 100%;
    font-family: "Lato", sans-serif;
    font-weight: 700;
    font-size: 22px;
    line-height: 34px;
    color: var(--services-text);
  }
</style>
</head>
<body>
  <section class="business-card">
    <h1 class="brand-name">Velora Aesthetics</h1>
    <p class="practitioner-name">Dr. Anjali Desai</p>
    <div class="rule rule--upper"></div>
    <div class="contact">
      <p><span class="contact__label">Phone:</span> 503-555-0142</p>
      <p>dr.anjali.desai@veloraaesthetics.com</p>
    </div>
    <div class="services">
      <p>Facial Aesthetics, Anti-wrinkle Treatment,</p>
      <p>Facial Volumisation &amp; Rejuvenation, Lip Volumisation.</p>
    </div>
    <div class="rule rule--lower"></div>
  </section>
</body>
</html>
```